BRIGHT COLORFUL + 55 FAMILY HISTORY BROCHURE 11 x 17 bifold

11 x 17 Bifold Flyer I have given you the Layout I just need you to make it Pretty

YOU DO NOT NEED TO FOLLOW MY LAYOUT, You can but dont have too

Target Market(s)

55 year old consumers, who could choose our service of Hereditary Cancer Screening

Industry/Entity Type

Health And Wellness

Requirements
Must have
• Must be appealing to Grand Parents, must make them want to test , show lots of pictures of grand children, YOU DO NOT NEED TO FOLLOW MY LAYOUT , You can but dont have too
Nice to have
• use our colors of our logo , YOU DO NOT NEED TO FOLLOW MY LAYOUT , You can but dont have too
Should not have
• YOU DO NOT NEED TO FOLLOW MY LAYOUT, You can but dont have too

```html
<!DOCTYPE html>
<html lang="en">
<head>
<meta charset="utf-8">
<title>Hereditary Cancer Screening Brochure</title>
<link rel="stylesheet" href="https://fonts.googleapis.com/css2?family=Raleway:wght@400;500;600;700;800&family=Oswald:wght@500&family=Comfortaa:wght@500&display=swap">
<style>
:root{
  --navy:#141d45;
  --navy-deep:#0f1638;
  --green:#7cc242;
  --green-dark:#5ea52c;
  --ink:#1c1c1c;
  --muted:#444;
  --stage:#e6e6e6;
  --paper:#ffffff;
}
*{margin:0;padding:0;box-sizing:border-box}
html,body{width:893px;height:1200px;overflow:hidden}
body{background:var(--stage);font-family:"Raleway",sans-serif;color:var(--ink);position:relative}
.spread{position:absolute;left:61px;width:771px;height:499px;background:var(--paper);overflow:hidden;box-shadow:0 1px 4px rgba(0,0,0,.18)}
.spread-outside{top:50px}
.spread-inside{top:618px}
.page{position:absolute;top:0;width:385.5px;height:499px;overflow:hidden}
.page-left{left:0}
.page-right{left:385.5px}
.page svg.bg{position:absolute;inset:0;width:100%;height:100%}
.photo{position:absolute}
.photo-circle{border-radius:50%;border:5px solid var(--green);box-shadow:0 1px 3px rgba(0,0,0,.25)}
.caption{position:absolute;left:0;width:893px;text-align:center;font-size:21px;letter-spacing:1px;color:#333;font-weight:400}
.txt{position:absolute}
.g{color:var(--green-dark);font-weight:700}
.brand{position:absolute;display:flex;align-items:center;gap:7px;white-space:nowrap}
.brand-dot{border-radius:50%;border:3px solid var(--navy);flex:none}
.brand-name{font-family:"Raleway",sans-serif;font-weight:700;color:var(--navy);line-height:1;letter-spacing:.5px}
.brand.on-dark .brand-dot{border-color:#fff}
.brand.on-dark .brand-name{color:#fff}
.url{position:absolute;font-size:7.4px;letter-spacing:1.2px;color:var(--green)}
.body-copy{font-size:6.3px;line-height:1.42;color:var(--muted);text-align:justify}
.body-copy p{margin-bottom:5px}
.corner-dot{position:absolute;width:32px;height:32px;border-radius:50%;border:3px solid var(--green);background:#fff}
</style>
</head>
<body>

<!-- OUTSIDE SPREAD -->
<section class="spread spread-outside">
  <div class="page page-left">
    <svg class="bg" viewBox="0 0 385.5 499" preserveAspectRatio="none">
      <rect width="385.5" height="499" fill="#fff"/>
      <path d="M130 0 C200 15 300 40 385.5 120 L385.5 0Z" fill="var(--green)"/>
    </svg>
    <div class="photo" role="img" aria-label="Grandfather being kissed by his granddaughter" style="left:-40px;top:-60px;width:190px;height:190px;border-radius:50%;border:6px solid var(--green);background:radial-gradient(circle at 55% 60%,#e9d9c8,#bfa690 60%,#8a7464)"></div>
    <div class="photo photo-circle" role="img" aria-label="Grandmother hugging her grandchildren" style="left:152px;top:16px;width:112px;height:112px;background:radial-gradient(circle at 50% 55%,#a77a5a,#6b4a36 70%,#3c2a20)"></div>
    <div class="photo photo-circle" role="img" aria-label="Three generations of a family sitting in a garden" style="left:270px;top:56px;width:96px;height:96px;background:radial-gradient(circle at 50% 55%,#d9cbb8,#9aa57f 65%,#6c7a55)"></div>
    <div class="txt" style="left:25px;top:179px;width:350px;font-size:16px;font-weight:500;letter-spacing:.2px"><span style="color:var(--green);font-weight:800">DOES CANCER</span> RUN IN YOUR FAMILY?</div>
    <div class="txt" style="left:25px;top:200px;width:350px;font-size:12.6px;font-weight:500"><b style="font-weight:800">A Simple Swab</b> Could SAVE a Family Members LIFE</div>
    <div class="txt" style="left:25px;top:226px;width:340px;font-size:9.6px;line-height:1.4;text-align:center;color:#333">Your decision won’t just affect you. It will also impact Your Family,<br>since your test results may Forecast Their Cancer Risks, too.</div>
    <div class="photo" role="img" aria-label="Smiling extended family of grandparents, parents and children" style="left:0;top:254px;width:385.5px;height:100px;background:linear-gradient(180deg,rgba(255,255,255,.9),rgba(220,214,200,.7) 30%,#cdbfa9 70%,rgba(240,236,228,.6));-webkit-mask:linear-gradient(90deg,transparent,#000 15%,#000 85%,transparent);mask:linear-gradient(90deg,transparent,#000 15%,#000 85%,transparent)"></div>
    <svg class="bg" viewBox="0 0 385.5 499" preserveAspectRatio="none" style="pointer-events:none">
      <path d="M0 330 C120 390 260 400 385.5 300 L385.5 499 L0 499Z" fill="var(--navy)"/>
      <path d="M0 315 C120 380 260 385 385.5 290 L385.5 300 C260 398 120 392 0 332Z" fill="var(--green)"/>
    </svg>
    <div class="brand on-dark" style="left:14px;top:424px;gap:5px">
      <span class="brand-dot" style="width:24px;height:24px;border-width:2.5px"></span>
      <span class="brand-name" style="font-size:7.8px;letter-spacing:.2px">KINWELL HEALTH GROUP</span>
    </div>
    <div class="txt" style="left:149px;top:398px;width:220px;font-size:6.6px;line-height:1.5;color:#dfe3ef;text-align:justify"><span class="g" style="color:var(--green);font-size:7.2px">We believe it is important to understand what can and cannot be learned with genetic testing.</span> Genetic mutations can increase risks for certain cancers, but this does not mean cancer will definitely develop. You should be prepared to receive positive or negative results. Most people receive Negative Results meaning no mutations associated with an increased risk for the Hereditary cancers.</div>
    <div class="url" style="left:148px;top:478px">www.KinwellScreening.example</div>
  </div>

  <div class="page page-right">
    <svg class="bg" viewBox="0 0 385.5 499" preserveAspectRatio="none">
      <rect width="385.5" height="499" fill="var(--navy)"/>
    </svg>
    <div class="photo" role="img" aria-label="Elderly hand holding a small child's hand outdoors" style="left:0;top:40px;width:385.5px;height:260px;background:linear-gradient(135deg,#6f7d3a,#a9a25a 35%,#d6b89a 55%,#8fa1b8 75%,#5f7a4a)"></div>
    <svg class="bg" viewBox="0 0 385.5 499" preserveAspectRatio="none">
      <path d="M0 0 L385.5 0 L385.5 60 C300 130 140 140 0 90Z" fill="#fff"/>
      <path d="M0 90 C140 140 300 130 385.5 60 L385.5 70 C300 145 140 152 0 100Z" fill="var(--green)"/>
      <path d="M0 300 C120 270 260 270 385.5 300 L385.5 499 L0 499Z" fill="var(--navy)"/>
      <path d="M0 290 C120 262 260 262 385.5 290 L385.5 300 C260 272 120 272 0 300Z" fill="var(--green)"/>
    </svg>
    <div class="brand" style="left:82px;top:32px">
      <span class="brand-dot" style="width:40px;height:40px"></span>
      <span class="brand-name" style="font-size:14.5px">KINWELL HEALTH GROUP</span>
    </div>
    <div class="photo photo-circle" role="img" aria-label="Grandfather and grandson looking at something together" style="left:17px;top:246px;width:104px;height:104px;background:radial-gradient(circle at 50% 55%,#b59a78,#6d7a4c 70%,#3f4a2d)"></div>
    <div class="photo photo-circle" role="img" aria-label="Grandmother cheek to cheek with a granddaughter" style="left:140px;top:236px;width:112px;height:112px;background:radial-gradient(circle at 50% 55%,#e8d6c3,#b49a84 70%,#6a7b58)"></div>
    <div class="photo photo-circle" role="img" aria-label="Grandparents with a smiling grandchild" style="left:268px;top:240px;width:108px;height:108px;background:radial-gradient(circle at 50% 55%,#e2cbb3,#a78c74 70%,#58704a)"></div>
    <div class="txt" style="left:0;top:372px;width:385.5px;text-align:center;font-family:'Oswald',sans-serif;font-weight:500;font-size:24px;color:#fff;letter-spacing:.3px;transform:scaleX(.92)">HEREDITARY CANCER SCREENING</div>
    <div class="txt" style="left:0;top:407px;width:385.5px;text-align:center;font-family:'Comfortaa',sans-serif;font-size:12.5px;color:var(--green)">"The Test You Take For Them"</div>
    <div class="txt" style="left:0;top:429px;width:385.5px;text-align:center;font-size:12.5px;color:#fff;line-height:1.3">Will You give Your loved ones the<br><span style="color:var(--green);font-weight:700">Information to Beat Cancer in their lives ?</span></div>
    <div class="url" style="left:128px;top:478px">www.KinwellScreening.example</div>
  </div>
</section>
<div class="caption" style="top:566px">BROCHURE OUTSIDE</div>

<!-- INSIDE SPREAD -->
<section class="spread spread-inside">
  <div class="page page-left">
    <div class="photo" role="img" aria-label="Grandmother and mother smiling over a sleeping baby" style="left:0;top:0;width:385.5px;height:150px;background:linear-gradient(120deg,#c9a98c,#e8d3bf 40%,#f3e6da 60%,#f7efe8)"></div>
    <svg class="bg" viewBox="0 0 385.5 499" preserveAspectRatio="none">
      <path d="M0 138 C120 160 260 150 385.5 120 L385.5 499 L0 499Z" fill="#fff"/>
      <path d="M0 130 C120 155 260 145 385.5 112 L385.5 120 C260 152 120 162 0 140Z" fill="var(--green)"/>
      <rect y="470" width="385.5" height="29" fill="var(--navy)"/>
      <rect y="468" width="385.5" height="2" fill="var(--green)"/>
    </svg>
    <div class="txt" style="left:0;top:170px;width:385.5px;text-align:center;font-size:11.5px;font-weight:700;color:var(--navy)"><span style="display:inline-block;width:32px;border-top:1px solid var(--green);vertical-align:middle;margin-right:8px"></span>Genetic Testing Saved My Life<span style="display:inline-block;width:32px;border-top:1px solid var(--green);vertical-align:middle;margin-left:8px"></span></div>
    <div class="txt body-copy" style="left:25px;top:193px;width:338px">
      <p><span class="g">Genetic testing revealed</span> Daniel Marsh carried a mutation that gave him a 55 to 70 percent chance of developing stomach cancer. Early screening revealed there were 14 sites of stage 1A cancer. Once the news sunk in, he realized <span class="g">his Mother’s Genetic Testing Saved His Life.</span></p>
      <p><span class="g">Genetic Testing Saved My Life,</span> Because of my age and <span class="g">Ashkenazi Jewish ancestry</span>, My Dr recommended Genetic Testing and they were right. I had the BRCA Gene, because of this my other two sister got tested, my younger sister was positive and my older sister was negative. <span class="g">Now we are in control,</span> there are steps that can be taken to reduce the risks, including enhanced breast cancer screening, risk-reducing surgeries, and chemoprevention, in which drugs are used to try to reduce the risk or delay the development of cancer.</p>
      <p><span class="g">A breast cancer survivor before age 30:</span> ‘Genetic testing saved my life’ Rachel Owens was diagnosed with breast cancer two weeks before her 29th birthday. Owens, now 30, credits her recovery to <span class="g">awareness of a hereditary genetic mutation</span> that predisposed her and her family to the disease. <span class="g">After my mom tested positive for the BRCA 1 gene mutation,</span> I knew genetic testing was something that I would need. Once <span class="g">I tested positive,</span> I was referred to a breast health clinic for <span class="g">increased surveillance.</span> There, my medical care providers were very diligent in making sure I was watched closely. <span class="g">Knowledge is power</span> and, in this case, <span class="g">Genetic testing saved my life!</span></p>
      <p><span class="g">My father had genetic testing</span> and found he had hereditary nonpolyposis colorectal cancer (HNPCC) commonly known as Lynch syndrome. My name is Margaret Hale and I am a 10-year survivor of colorectal cancer. From an early age I learned the importance of screenings and knew about signs and symptoms. <span class="g">Following screening guidelines for individuals at an increased risk &amp; Knowing my family history saved my life!</span></p>
    </div>
    <div class="txt" style="left:0;top:412px;width:385.5px;text-align:center;font-size:9.4px;font-weight:600;line-height:1.38;color:var(--green-dark)">A Positive result or finding a mutation is Not a Cancer<br>Diagnosis and does not mean you will ever develop Cancer</div>
    <div class="txt" style="left:0;top:442px;width:385.5px;text-align:center;font-size:9.4px;font-weight:600;line-height:1.38;color:var(--ink)">Learning if you have an increased risk for cancer<br>can make a difference</div>
    <span class="corner-dot" style="left:22px;top:460px"></span>
    <div class="url" style="left:118px;top:481px">www.KinwellScreening.example</div>
  </div>

  <div class="page page-right">
    <svg class="bg" viewBox="0 0 385.5 499" preserveAspectRatio="none">
      <rect width="385.5" height="499" fill="#fff"/>
      <path d="M0 0 L385.5 0 L385.5 160 C300 130 150 120 0 120Z" fill="var(--navy)"/>
      <path d="M0 112 C150 112 300 122 385.5 150 L385.5 165 C300 138 150 126 0 124Z" fill="var(--green)"/>
      <path d="M0 120 C150 126 300 136 385.5 162 L385.5 499 L0 499Z" fill="#fff"/>
      <rect y="470" width="385.5" height="29" fill="var(--navy)"/>
      <rect y="468" width="385.5" height="2" fill="var(--green)"/>
    </svg>
    <div class="photo photo-circle" role="img" aria-label="Grandparents with grandchildren lying on the grass" style="left:20px;top:40px;width:104px;height:104px;background:radial-gradient(circle at 50% 55%,#e1c9ae,#9fb07a 70%,#5d7a42)"></div>
    <div class="photo photo-circle" role="img" aria-label="Three generation family posing together" style="left:138px;top:28px;width:110px;height:110px;background:radial-gradient(circle at 50% 55%,#efe3d6,#c5ab94 70%,#7d6655)"></div>
    <div class="photo photo-circle" role="img" aria-label="Large family group gathered outdoors" style="left:262px;top:40px;width:104px;height:104px;background:radial-gradient(circle at 50% 55%,#e6d0b8,#a4b38a 70%,#5e7746)"></div>
    <div class="txt body-copy" style="left:24px;top:164px;width:340px">
      <p><span class="g" style="font-weight:600">Genetic Testing</span> is done to determine whether family members without obvious illness have inherited the same mutation as a family member who is known to carry a cancer associated mutation. Meaning <span class="g">Will You Help Your Kids &amp; Grand Children</span></p>
      <p style="margin-top:9px"><span class="g">What are the benefits of testing?</span> “The Power of Knowledge”. <span class="g">Helping younger Family Members know if there is a risk of Cancer and preparing for it.</span> knowing if you have a genetic mutation is that you can work with your doctor to monitor and address your cancer risks. According to the <span class="g">National Cancer Council eating 5 or more Servings of Vegetables &amp; Fruit, and Most Importantly also lowering your intake of red meat, dairy and eggs will help prevent or delay cancer.</span></p>
      <p style="margin-top:9px"><span class="g">There are many benefits to getting tested,</span> regardless of the eventual result. If one of your family members — however distant — had cancer, there is a chance that you inherited a gene mutation that not only increases your personal risk of cancer, but also could be passed to the next generation. Those who are carriers of hereditary cancer gene mutations, could be at risk of getting cancer earlier in life than the general population. <span class="g">The sooner genetic testing is done, the more likely it is that the risk can be managed appropriately.</span></p>
    </div>
    <div class="txt" style="left:0;top:322px;width:385.5px;text-align:center;font-size:10px;font-weight:500;line-height:1.3;color:var(--green-dark)">There are many Known risk factors for Cancer.<br><span style="color:var(--navy);font-weight:600">GENETICS and FAMILY HISTORY are Often Overlooked.</span></div>
    <div class="photo" role="img" aria-label="Grandparents playing with a grandson and baby in a sunny garden" style="left:0;top:345px;width:385.5px;height:123px;background:linear-gradient(180deg,rgba(255,255,255,1),rgba(190,198,160,.8) 30%,#a6a878 60%,#7f8a5a);"></div>
    <span class="corner-dot" style="left:330px;top:460px"></span>
    <div class="url" style="left:118px;top:481px">www.KinwellScreening.example</div>
  </div>
</section>
<div class="caption" style="top:1139px">BROCHURE INSIDE</div>

</body>
</html>
```